Rate sheet redesign

We provide rate sheets to agents for our scenic flights and I would like to make them easier to read and more comprehensive. I'd also like to be able to edit the information in the design, as tours get updated and so do the rates. We've got new product out of shark bay, so the sections would need to be: Perth, Geraldton, Kalbarri and Shark Bay. I've attached what we've been using and also some concept photos.

also a link to our flights online: https://coralwingtours.bookvista.com/catalog/418752/flights-from-perth

I've put this under brochure redesign as I wasn't sure what a rate sheet would be considered. Open to different formats if it means content is editable.

Need extra days to review

```html
<!DOCTYPE html>
<html lang="en">
<head>
<meta charset="utf-8">
<title>Geraldton Rates – Coralwing Aviation</title>
<link href="https://fonts.googleapis.com/css2?family=Bebas+Neue&family=Montserrat:wght@400;500;600;700;800&display=swap" rel="stylesheet">
<style>
  :root {
    --blue: #0457a0;
    --orange: #f0982a;
    --ink: #111318;
    --sheet-top: #d9e8f2;
    --sheet-bottom: #edf1f5;
    --cell: #ffffff;
    --photo-sky: #a8d4e8;
    --photo-pale: #cfe6f0;
    --photo-green: #d7e6c8;
    --photo-sand: #f0d9a6;
    --photo-peach: #f3c39a;
  }
  html, body { margin: 0; padding: 0; width: 1200px; height: 903px; overflow: hidden; }
  body { font-family: "Montserrat", Arial, sans-serif; color: var(--ink); }
  .rate-sheet {
    position: relative; width: 1200px; height: 903px; overflow: hidden;
    background: linear-gradient(135deg, var(--sheet-top) 0%, var(--sheet-bottom) 100%);
  }
  .travel-photo {
    position: absolute; left: 0; top: 0; width: 380px; height: 903px;
    background:
      radial-gradient(ellipse 220px 260px at 150px 150px, var(--photo-sand) 0%, rgba(240,217,166,0) 70%),
      radial-gradient(ellipse 200px 240px at 60px 300px, var(--photo-green) 0%, rgba(215,230,200,0) 70%),
      radial-gradient(ellipse 90px 200px at 10px 470px, var(--photo-peach) 0%, rgba(243,195,154,0) 75%),
      radial-gradient(ellipse 200px 170px at 230px 470px, var(--photo-pale) 0%, rgba(207,230,240,0) 80%),
      linear-gradient(180deg, #dfe9e2 0%, #c4e0ec 45%, var(--photo-sky) 100%);
    -webkit-mask-image: linear-gradient(90deg, #000 80%, transparent 100%);
            mask-image: linear-gradient(90deg, #000 80%, transparent 100%);
  }
  .title { position: absolute; left: 393px; margin: 0; font-family: "Bebas Neue", Impact, sans-serif; font-weight: 400; line-height: 1; }
  .title-place { top: 48px; font-size: 112px; color: var(--blue); }
  .title-rates { top: 143px; font-size: 112px; color: var(--orange); }
  .validity { position: absolute; left: 395px; top: 250px; margin: 0; font-size: 14px; font-weight: 600; line-height: 18.5px; text-transform: uppercase; }
  .rule { position: absolute; left: 395px; top: 291px; width: 199px; height: 2px; background: var(--blue); }
  .rate-type { position: absolute; left: 394px; top: 296px; margin: 0; font-size: 27px; line-height: 34px; font-weight: 800; color: var(--orange); }
  .brand { position: absolute; left: 840px; top: 100px; width: 270px; text-align: center; font-size: 34px; font-weight: 700; line-height: 50px; color: var(--blue); }
  .rates-table {
    position: absolute; left: 395px; top: 457px;
    display: grid; grid-template-columns: 185px 249px 147px 81px 77px;
    grid-template-rows: 52px 98px 98px 98px; gap: 6px 6px;
    transform: translateY(-101px);
  }
  .cell { display: flex; align-items: center; justify-content: center; text-align: center; padding: 0 12px; font-size: 9.3px; line-height: 11px; background: var(--cell); }
  .cell.clause { padding: 0 16px; }
  .head { color: #fff; font-size: 11px; font-weight: 700; letter-spacing: .3px; }
  .head.orange { background: var(--orange); }
  .head.blue { background: var(--blue); }
  .cell p { margin: 0; }
  .cell p + p { margin-top: 11px; }
  .note { position: absolute; left: 395px; top: 741px; width: 800px; margin: 0; font-size: 14.6px; line-height: 19px; font-weight: 500; letter-spacing: .25px; white-space: nowrap; }
</style>
</head>
<body>
<main class="rate-sheet">
  <div class="travel-photo" role="img" aria-label="Photo of a folded world map, a map-print travel pouch and a white toy aeroplane on a pale blue surface"></div>

  <h1 class="title title-place">Geraldton</h1>
  <h2 class="title title-rates">Rates</h2>
  <p class="validity">Tour rates valid from 1st April<br>2025 to 31st March 2026</p>
  <div class="rule"></div>
  <h3 class="rate-type">RETAIL RATES</h3>

  <div class="brand">Coralwing<br>Aviation</div>

  <section class="rates-table">
    <div class="cell head orange">FLIGHT</div>
    <div class="cell head blue">INCLUSIONS</div>
    <div class="cell head orange">CLAUSES</div>
    <div class="cell head blue">ADULT</div>
    <div class="cell head blue">CHILD</div>

    <div class="cell">Abrolhos Island Discovery Tour<br>(Flight 303)</div>
    <div class="cell"><div><p>Included: Scenic flight from Geraldton to East Wallabi Island return. Morning /Afternoon Tea, and snorkel gear.</p><p>Duration: 1 hour 20 minutes flight time<br>5 hours 30 minutes Total Tour time</p></div></div>
    <div class="cell clause">Normal departure time is 8am, however timing is flexible depending on bookings. Start time must be 6 hours before sunset.</div>
    <div class="cell">$550.00</div>
    <div class="cell">$385.00</div>

    <div class="cell">Abrolhos Island Discovery Tour<br>plus Pink Lake (Flight 304)</div>
    <div class="cell"><div><p>Included: Scenic flight from Geraldton to East Wallabi Island return via Pink Lake. Morning /Afternoon Tea, and snorkel gear.</p><p>Duration: 2 hours flight time<br>6 hours Total Tour time</p></div></div>
    <div class="cell clause">Normal departure time is 8am, however timing is flexible depending on bookings. Start time must be 6 hours before sunset.</div>
    <div class="cell">$610.00</div>
    <div class="cell">$427.00</div>

    <div class="cell">Abrolhos Islands and Batavia<br>Shipwreck (Flight 303B)</div>
    <div class="cell"><div><p>Included: Scenic flight from Geraldton to East Wallabi Island return, and Morning /Afternoon Tea.</p><p>Duration: 1 hour 20 minutes flight time<br>2 hours Total Tour time</p></div></div>
    <div class="cell clause">Normal departure time is 2pm, however timing is flexible depending on bookings. Start time must be 2.5 hours before sunset.</div>
    <div class="cell">$500.00</div>
    <div class="cell">$350.00</div>
  </section>

  <p class="note">Please Note There Is A New $11 Government Fee For All Flights Landing At The Abrolhos Islands,<br>This Is Not A Commissionable Fee And Needs To Be Paid On Top Of The Nett Rate</p>
</main>
</body>
</html>
```